Business Card design for new private practice opening

I need a business card design for my new private practice with my new logo uploaded as a file
On the front the logo
On the back: maybe a small logo somewhere?
Priv. Doz. DDr. Corinna Vestaluk
Fachärztin für Allgemein- & Viszeralchirurgie
Address: xxx
Tel: xxx
Mobil:xxx
Webseite:xxx
Email:xxx

Contact Information for Business Card

See project description above for details

Requirements
Nice to have
• I would like the colors of the logo incorporated into the business card

```html
<!DOCTYPE html>
<html lang="de">
<head>
<meta charset="UTF-8">
<title>Vestaluk Chirurgie – Visitenkarte</title>
<link rel="stylesheet" href="https://fonts.googleapis.com/css2?family=Raleway:wght@400;500;600&display=swap">
<style>
  :root {
    --bg: #e9eaea;
    --card: #ffffff;
    --teal: #4fbcb6;
    --grey: #8a8a8a;
    --ink: #2a2a2a;
    --ink-soft: #444444;
    --icon: #8f8f8f;
  }
  * { box-sizing: border-box; margin: 0; padding: 0; }
  html, body {
    width: 1200px; height: 1200px; overflow: hidden;
    background: var(--bg);
    font-family: "Raleway", sans-serif;
  }
  .canvas {
    position: relative; width: 1200px; height: 1200px;
  }
  .card {
    position: absolute; top: 434px;
    width: 500px; height: 332px;
    background: var(--card);
    overflow: hidden;
  }
  .card--front { left: 62px; }
  .card--back { left: 638px; }

  .card-edge {
    position: absolute; left: 0; right: 0; bottom: 0;
    height: 9px; background: var(--teal);
  }

  .brand {
    display: flex; align-items: center;
    color: var(--grey); font-weight: 600;
    text-transform: uppercase; letter-spacing: 0.02em;
  }
  .brand-dot {
    flex: none; border-radius: 50%;
    background: var(--teal);
  }
  .brand--large {
    position: absolute; left: 76px; top: 102px;
    gap: 18px; font-size: 38px; line-height: 1.12;
  }
  .brand--large .brand-dot { width: 112px; height: 112px; }

  .brand--small {
    position: absolute; left: 50%; top: 38px; transform: translateX(-50%);
    gap: 12px; font-size: 24px; line-height: 1.1;
  }
  .brand--small .brand-dot { width: 62px; height: 62px; }

  .holder {
    position: absolute; left: 0; right: 0; top: 146px;
    text-align: center;
  }
  .holder-name {
    font-size: 24px; font-weight: 500; color: var(--ink);
  }
  .holder-title {
    margin-top: 6px; font-size: 17px; font-weight: 400; color: var(--ink-soft);
  }

  .contacts {
    position: absolute; left: 70px; right: 40px; top: 228px;
    display: grid; grid-template-columns: 210px 1fr;
    row-gap: 8px; column-gap: 0;
    font-size: 16.5px; color: var(--ink-soft);
  }
  .contact { display: flex; align-items: center; gap: 9px; }
  .contact svg { width: 16px; height: 16px; flex: none; fill: var(--icon); }
</style>
</head>
<body>
<main class="canvas">

  <section class="card card--front" aria-label="Vorderseite">
    <div class="brand brand--large">
      <span class="brand-dot"></span>
      <span class="brand-name">Vestaluk<br>Chirurgie</span>
    </div>
    <div class="card-edge"></div>
  </section>

  <section class="card card--back" aria-label="Rückseite">
    <div class="brand brand--small">
      <span class="brand-dot"></span>
      <span class="brand-name">Vestaluk<br>Chirurgie</span>
    </div>

    <div class="holder">
      <p class="holder-name">Priv. Doz. DDr. Corinna Vestaluk</p>
      <p class="holder-title">Fachärztin für Allgemein- &amp; Viszeralchirurgie</p>
    </div>

    <div class="contacts">
      <div class="contact">
        <svg viewBox="0 0 16 16"><path d="M8 1.5 1 7.5h2v7h4v-4h2v4h4v-7h2z"/></svg>
        <span>Address: xxx</span>
      </div>
      <div></div>
      <div class="contact">
        <svg viewBox="0 0 16 16"><path d="M3.6 1.2 5.8 3.4c.4.4.4 1 0 1.4L4.7 5.9c.8 2 2.6 3.9 4.6 4.7l1.1-1.1c.4-.4 1-.4 1.4 0l2.2 2.2c.4.4.4 1 0 1.4l-1.2 1.2c-.8.8-2 .9-3 .4C6.4 13.2 3 9.8 1.4 6.4c-.5-1-.4-2.2.4-3z"/></svg>
        <span>Tel: xxx</span>
      </div>
      <div class="contact">
        <svg viewBox="0 0 16 16"><path d="M8 1a7 7 0 1 0 0 14A7 7 0 0 0 8 1zm0 1.3c.7 0 1.6 1.4 2 3.7H6c.4-2.3 1.3-3.7 2-3.7zM5.9 7.3h4.2a13 13 0 0 1 0 1.4H5.9a13 13 0 0 1 0-1.4zM2.4 7.3h2.2v1.4H2.4a5.7 5.7 0 0 1 0-1.4zm9 0h2.2a5.7 5.7 0 0 1 0 1.4h-2.2a15 15 0 0 0 0-1.4zM6 10h4c-.4 2.3-1.3 3.7-2 3.7S6.4 12.3 6 10zm-3.1 0h1.8c.2 1.3.5 2.4 1 3.2A5.7 5.7 0 0 1 2.9 10zm8.4 0h1.8a5.7 5.7 0 0 1-2.8 3.2c.5-.8.8-1.9 1-3.2zM2.9 6a5.7 5.7 0 0 1 2.8-3.2c-.5.8-.8 1.9-1 3.2zm8.4 0c-.2-1.3-.5-2.4-1-3.2A5.7 5.7 0 0 1 13.1 6z"/></svg>
        <span>Webseite: xxx</span>
      </div>
      <div class="contact">
        <svg viewBox="0 0 16 16"><path d="M5 1h6a1 1 0 0 1 1 1v12a1 1 0 0 1-1 1H5a1 1 0 0 1-1-1V2a1 1 0 0 1 1-1zm.3 1.3v10.2h5.4V2.3zM7.2 13.2v.6h1.6v-.6z"/></svg>
        <span>Mobil: xxx</span>
      </div>
      <div class="contact">
        <svg viewBox="0 0 16 16"><path d="M1 3.5h14v9H1zm1.6 1.2L8 8.6l5.4-3.9zm-.3 1.4v5.2h11.4V6.1L8 10.2z"/></svg>
        <span>Email: xxx</span>
      </div>
    </div>
  </section>

</main>
</body>
</html>
```